Brightvolt Electrical Services Needs A Flyer Design

We need a flyer design for a new business based in Sydney, Australia called Brightvolt Electrical Services. We provide services for residential,commercial and industrial works. Services include Electrical Design, Installation, Repairs & Maintenance. Communications Installation, Cabling, Maintenance & Repairs. Over 25 years Industry Experience.Service Calls, Quick Response Time, Professional Service. We would like to see designs that use the colors red,white and blue similar to the logo. The final Design should be creative as the business logo suggests and should communicate the businesses services.

Target Market(s)

Residential

Industry/Entity Type

Industrial

Font styles to use
Sans Serif

Requirements
Must have
• My project must have the logo provided utilized in the flyer.It must list the following contact name and number Ray 0491 627 318 services as above in the project description. Flyer should be DL size (99mmx210mm).

```html
<!DOCTYPE html>
<html lang="en">
<head>
<meta charset="utf-8">
<title>Brightvolt Electrical Services – Flyer</title>
<link rel="stylesheet" href="https://fonts.googleapis.com/css2?family=Audiowide&family=Oswald:wght@600&family=Open+Sans:wght@700&family=PT+Sans+Narrow&display=swap">
<style>
  :root {
    --stage: #26282b;
    --paper: #ffffff;
    --red: #d0202e;
    --navy: #1b2a6b;
    --blue: #1d5f8e;
    --blue-deep: #153e66;
    --ink: #1a2146;
    --white: #ffffff;
  }
  html, body {
    margin: 0;
    width: 1200px;
    height: 1027px;
    overflow: hidden;
    background: var(--stage);
  }
  .flyer {
    position: absolute;
    left: 252px;
    top: 23px;
    width: 696px;
    height: 981px;
    display: block;
    box-shadow: 0 10px 30px rgba(0,0,0,.45);
  }
  .brand-name { font-family: "Audiowide", sans-serif; fill: var(--ink); }
  .sector { font-family: "Oswald", sans-serif; font-weight: 600; fill: var(--white); font-size: 27px; }
  .service { font-family: "Audiowide", sans-serif; fill: var(--ink); }
  .experience { font-family: "Open Sans", sans-serif; font-weight: 700; fill: var(--white); font-size: 17px; }
  .perk { font-family: "PT Sans Narrow", sans-serif; fill: var(--white); font-size: 17px; }
  .call { font-family: "Audiowide", sans-serif; fill: var(--white); font-size: 22px; }
</style>
</head>
<body>
<svg class="flyer" viewBox="0 0 579 816" xmlns="http://www.w3.org/2000/svg">
  <defs>
    <linearGradient id="bodyBlue" x1="0" y1="0" x2="0" y2="1">
      <stop offset="0" stop-color="var(--blue-deep)"/>
      <stop offset="0.5" stop-color="var(--blue)"/>
      <stop offset="1" stop-color="var(--blue-deep)"/>
    </linearGradient>
    <linearGradient id="whiteBand" x1="0" y1="0" x2="1" y2="0">
      <stop offset="0" stop-color="#ffffff"/>
      <stop offset="0.5" stop-color="#d9dde3"/>
      <stop offset="1" stop-color="#ffffff"/>
    </linearGradient>
    <radialGradient id="bulbGlow" cx="0.5" cy="0.45" r="0.5">
      <stop offset="0" stop-color="#f4ff6a"/>
      <stop offset="0.45" stop-color="#b9d93a" stop-opacity="0.85"/>
      <stop offset="1" stop-color="#2d7fb0" stop-opacity="0"/>
    </radialGradient>
    <radialGradient id="handTone" cx="0.5" cy="0.5" r="0.5">
      <stop offset="0" stop-color="#f0c2a4"/>
      <stop offset="1" stop-color="#c98c6e" stop-opacity="0.2"/>
    </radialGradient>
  </defs>

  <!-- header -->
  <rect class="header" x="0" y="0" width="579" height="138" fill="var(--paper)"/>
  <text class="brand-name" x="289.5" y="74" text-anchor="middle" font-size="36">BRIGHTVOLT</text>
  <text class="brand-name" x="289.5" y="100" text-anchor="middle" font-size="12" letter-spacing="2">ELECTRICAL SERVICES</text>
  <rect x="0" y="128" width="579" height="5" fill="var(--red)"/>

  <!-- body -->
  <rect class="body" x="0" y="138" width="579" height="606" fill="url(#bodyBlue)"/>

  <g class="sectors">
    <text class="sector" x="115" y="178" text-anchor="middle">Residential</text>
    <circle cx="202" cy="170" r="4" fill="var(--navy)"/>
    <text class="sector" x="285" y="178" text-anchor="middle">Commercial</text>
    <circle cx="391" cy="170" r="4" fill="var(--navy)"/>
    <text class="sector" x="472" y="178" text-anchor="middle">Industrial</text>
  </g>

  <!-- light bulb photo area -->
  <g role="img" aria-label="Photo of a glowing light bulb floating above an open hand">
    <circle cx="285" cy="330" r="175" fill="url(#bulbGlow)"/>
    <ellipse cx="300" cy="630" rx="260" ry="52" fill="url(#handTone)"/>
  </g>

  <!-- stripes -->
  <polygon points="0,313 579,188 579,250 0,355" fill="var(--red)" opacity="0.92"/>
  <polygon points="0,355 579,250 579,300 0,383" fill="url(#whiteBand)" opacity="0.85"/>
  <polygon points="0,383 579,398 579,458 0,441" fill="var(--red)" opacity="0.92"/>
  <polygon points="0,441 579,458 579,518 0,500" fill="url(#whiteBand)" opacity="0.92"/>
  <polygon points="0,500 579,518 579,577 0,562" fill="var(--navy)" opacity="0.92"/>

  <g class="services">
    <text class="service" font-size="28" transform="translate(96 336) rotate(-14)">Electrical Design</text>
    <text class="service" font-size="28" transform="translate(182 380) rotate(-14)">Installation</text>
    <text class="service" font-size="27" transform="translate(37 420) rotate(2)" textLength="505">Repairs &amp; Maintenance</text>
    <text class="service" font-size="23" transform="translate(38 478) rotate(1.5)" textLength="502">Communications Installation</text>
    <text class="service" font-size="24" transform="translate(88 536) rotate(1.5)" fill="var(--navy)" stroke="var(--white)" stroke-width="0.8">Cabling</text>
    <text class="service" font-size="15" transform="translate(352 541) rotate(1)" fill="var(--navy)" stroke="var(--white)" stroke-width="0.6">Maintenance &amp;</text>
    <text class="service" font-size="15" transform="translate(352 560) rotate(1)" fill="var(--navy)" stroke="var(--white)" stroke-width="0.6">Repairs</text>
  </g>

  <!-- experience -->
  <text class="experience" x="30" y="678">Over 25 years</text>
  <text class="experience" x="30" y="702">Industry Experience.</text>
  <g class="perks">
    <path d="M36 718 l4 5 l8 -11" fill="none" stroke="var(--white)" stroke-width="2.4"/>
    <text class="perk" x="54" y="727">Service Calls</text>
    <path d="M142 718 l4 5 l8 -11" fill="none" stroke="var(--white)" stroke-width="2.4"/>
    <text class="perk" x="160" y="727">Quick Response Time</text>
    <path d="M302 718 l4 5 l8 -11" fill="none" stroke="var(--white)" stroke-width="2.4"/>
    <text class="perk" x="320" y="727">Professional Service.</text>
  </g>

  <!-- footer -->
  <rect class="footer" x="0" y="744" width="579" height="72" fill="var(--red)"/>
  <text class="call" x="38" y="780" textLength="482">Call Us Now Ray 0491 627 318</text>
</svg>
</body>
</html>
```